Kbt

Spa brochure (tri-fold or bi-fold layout)

Target Market(s)

18-99 yrs old

Font styles to use
Sans Serif
Decorative

Colors
00a990
33b8a4
86cfc6
ffffff

Requirements
Must have
• high end appeal, larger font for ease of reading info, flow smoothly through all departments (massage, facials/waxing, nails, vichy and hair)
Nice to have
• map with address
Should not have
• confusion or spelling errors

```html
<!DOCTYPE html>
<html lang="en">
<head>
<meta charset="utf-8">
<title>Kbt Spa Menu</title>
<link href="https://fonts.googleapis.com/css2?family=Aladin&family=Montserrat:wght@400;600;700&display=swap" rel="stylesheet">
<style>
:root{
  --teal:#00a990;
  --teal-mid:#33b8a4;
  --teal-light:#86cfc6;
  --white:#ffffff;
  --ink:#1d2b2a;
}
*{box-sizing:border-box;margin:0;padding:0}
html,body{width:1200px;height:927px;overflow:hidden}
body{
  position:relative;
  font-family:"Montserrat",sans-serif;
  background:linear-gradient(90deg,var(--teal) 0%,var(--teal) 24%,var(--teal-mid) 27%,var(--teal) 30%,var(--teal) 48%,var(--teal-mid) 51%,var(--teal) 54%,var(--teal) 72%,var(--teal-light) 75%,var(--teal) 78%,var(--teal) 95%,var(--teal-mid) 100%);
}
.panel{
  position:absolute;
  background:var(--white);
  padding:0 6px 6px;
  display:flex;flex-direction:column;
}
.panel-title{
  font-family:"Aladin",cursive;
  font-weight:400;
  color:var(--teal);
  font-size:35px;
  text-align:center;
  height:39px;line-height:42px;
  white-space:nowrap;
}
.section{
  background:var(--teal);
  color:var(--white);
  font-weight:700;
  font-size:16.5px;
  text-align:center;
  line-height:22px;
  padding:4px 4px;
}
.price-row{
  background:var(--teal-light);
  color:var(--ink);
  font-weight:400;
  font-size:18px;
  display:flex;justify-content:space-between;
  height:31px;align-items:center;
  padding:0 14px 0 28px;
}
.lined .price-row{border-bottom:2px solid var(--white);height:30.6px;padding:0 8px 0 22px}
.lined .price-row:last-child{border-bottom:none}
.pkg-item{
  background:var(--teal-light);
  color:var(--ink);
  font-size:18px;
  line-height:22px;
  text-align:center;
  padding:4px 10px;
}
.massages{left:34px;top:25px;width:252px;height:457px}
.facials{left:328px;top:25px;width:252px;height:429px}
.waxing{left:622px;top:25px;width:252px;height:389px}
.hands-feet{left:622px;top:432px;width:252px;height:308px}
.wetroom{left:622px;top:766px;width:252px;height:144px}
.packages{left:916px;top:25px;width:252px;height:681px}
.waxing .panel-title{padding-bottom:4px;height:43px}
.hands-feet .panel-title{height:48px;line-height:52px}
.wetroom .panel-title{height:44px;line-height:50px}
.pkg-item.last{flex:1}
.team-photo{
  position:absolute;left:0;top:498px;width:578px;height:429px;
  background:linear-gradient(180deg,#4a4743 0%,#2b2522 55%,#3a2a22 100%);
}
.nail-photo{
  position:absolute;left:918px;top:730px;width:282px;height:197px;
  background:linear-gradient(135deg,#c9324a 0%,#e0567f 45%,#d98bb0 100%);
}
</style>
</head>
<body>

<section class="panel massages">
  <h2 class="panel-title">Massages</h2>
  <div class="section">Serene Massage</div>
  <div class="price-row"><span>45 min</span><span>$75</span></div>
  <div class="price-row"><span>75 min</span><span>$105</span></div>
  <div class="price-row"><span>105 min</span><span>$140</span></div>
  <div class="section">Stonehaven Hot Stone Massage</div>
  <div class="price-row"><span>75 min</span><span>$135</span></div>
  <div class="price-row"><span>105 min</span><span>$170</span></div>
  <div class="section">Chakra Balancing<br>Massage</div>
  <div class="price-row"><span>75 min</span><span>$105</span></div>
  <div class="section">Side-by-Side Massage</div>
  <div class="price-row"><span>75 min</span><span>$180</span></div>
  <div class="price-row"><span>105 min</span><span>$240</span></div>
</section>

<section class="panel facials">
  <h2 class="panel-title">Facials</h2>
  <div class="section">Aurelle Goddess Facial<br>Gentlemen’s Facial</div>
  <div class="price-row"><span>45 min</span><span>$75</span></div>
  <div class="price-row"><span>75 min</span><span>$105</span></div>
  <div class="price-row"><span>105 min</span><span>$140</span></div>
  <div class="section">Luminara Anti-Aging Facial</div>
  <div class="price-row"><span>75 min</span><span>$130</span></div>
  <div class="price-row"><span>105 min</span><span>$160</span></div>
  <div class="section">Chakra Balancing<br>Massage</div>
  <div class="price-row"><span>75 min</span><span>$105</span></div>
  <div class="section">Back Facial Treatment</div>
  <div class="price-row"><span>45 min</span><span>$75</span></div>
</section>

<section class="panel waxing">
  <h2 class="panel-title">Waxing and Tinting</h2>
  <div class="lined">
    <div class="price-row"><span>Brow Tint</span><span>$15</span></div>
    <div class="price-row"><span>Lash Tint</span><span>$15</span></div>
    <div class="price-row"><span>Brow Wax</span><span>$20</span></div>
    <div class="price-row"><span>Lip or Chin</span><span>$15</span></div>
    <div class="price-row"><span>Full Face</span><span>$50</span></div>
    <div class="price-row"><span>Underarms</span><span>$25</span></div>
    <div class="price-row"><span>Arms</span><span>$30+</span></div>
    <div class="price-row"><span>Lower Legs</span><span>$40</span></div>
    <div class="price-row"><span>Full Legs</span><span>$75</span></div>
    <div class="price-row"><span>Simple Bikini</span><span>$35+</span></div>
    <div class="price-row"><span>Back or Chest</span><span>$50+</span></div>
  </div>
</section>

<section class="panel hands-feet">
  <h2 class="panel-title">Hands and Feet</h2>
  <div class="section">Pedicure</div>
  <div class="price-row"><span>Spa</span><span>$60</span></div>
  <div class="price-row"><span>Express</span><span>$45</span></div>
  <div class="section">Manicure</div>
  <div class="price-row"><span>Spa</span><span>$40</span></div>
  <div class="price-row"><span>Express</span><span>$25</span></div>
  <div class="section">Reflexology</div>
  <div class="price-row"><span>45 min</span><span>$60</span></div>
</section>

<section class="panel wetroom">
  <h2 class="panel-title">Vishy Wetroom</h2>
  <div class="section">Hydrotherapy</div>
  <div class="price-row"><span>45 min</span><span>$90</span></div>
  <div class="price-row"><span>75 min</span><span>$120</span></div>
</section>

<section class="panel packages">
  <h2 class="panel-title">Packages</h2>
  <div class="section">Platinum - $360</div>
  <div class="pkg-item">105 min Stonehaven Hot Stone Massage</div>
  <div class="pkg-item">105 min Luminara Anti-Aging Facial</div>
  <div class="pkg-item">Spa Pedicure</div>
  <div class="pkg-item">Spa Manicure</div>
  <div class="section">Gold - $230</div>
  <div class="pkg-item">75 min Serene Massage</div>
  <div class="pkg-item">75 min Aurelle Goddess Facial or Gentleman’s Facial</div>
  <div class="pkg-item">Spa Pedicure</div>
  <div class="section">Silver - $180</div>
  <div class="pkg-item">75 min Serene Massage</div>
  <div class="pkg-item">75 min Aurelle Goddess Facial or Gentleman’s Facial</div>
  <div class="section">Bronze - $130</div>
  <div class="pkg-item">45 min Serene Massage</div>
  <div class="pkg-item last">45 min Aurelle Goddess Facial or Gentleman’s Facial</div>
</section>

<div class="team-photo" role="img" aria-label="Photo of the spa team standing together in the reception area"></div>
<div class="nail-photo" role="img" aria-label="Close-up photo of rows of pink and red nail polish bottles"></div>

</body>
</html>
```